KVRD Pinecrest Rehabilitation Consultants, INC
Business Card and Stationary for KVRD Pinecrest Rehabilitation
Professional
Dorian K. Lumbard, Ph. D.
Vocational Rehabilitation Consultant
4173b GA Hwy 508 STE 612 Conyers, GA 30081
Dorian.Lumbard@kvrdpinecrestrehab.example
www.kvrdpinecrestrehab.example
I will need whole set of stationary, letterhead, envelopes etc.

```html
<!DOCTYPE html>
<html lang="en">
<head>
<meta charset="utf-8">
<title>KVRD Pinecrest Rehabilitation – Business Card</title>
<link rel="stylesheet" href="https://fonts.googleapis.com/css2?family=Open+Sans:wght@400;600;700&display=swap">
<style>
  :root {
    --bg: #e4e5e7;
    --royal: #2f4fae;
    --royal-deep: #23409c;
    --royal-light: #4a72d6;
    --navy: #1d3a7a;
    --ink: #4a4f57;
    --muted: #7b8089;
    --paper: #ffffff;
  }
  * { margin: 0; padding: 0; box-sizing: border-box; }
  html, body { width: 1200px; height: 902px; overflow: hidden; }
  body {
    background: var(--bg);
    font-family: "Open Sans", Arial, sans-serif;
    position: relative;
  }
  .card {
    position: absolute;
    width: 620px;
    height: 354px;
    overflow: hidden;
    box-shadow: 0 6px 18px rgba(0,0,0,0.18);
  }
  /* back side */
  .card-back {
    left: 470px; top: 60px;
    background: linear-gradient(135deg, var(--royal-light) 0%, var(--royal) 45%, var(--royal-deep) 100%);
  }
  .card-back .web {
    position: absolute;
    left: 0; right: 0; top: 162px;
    text-align: center;
    color: var(--paper);
    font-size: 20px;
    letter-spacing: 2px;
    white-space: nowrap;
  }
  .web strong { font-weight: 700; }
  /* front side */
  .card-front {
    left: 130px; top: 480px;
    background: var(--paper);
  }
  .band { position: absolute; left: 0; bottom: 0; width: 620px; height: 120px; }
  .brand {
    position: absolute;
    left: 40px; top: 60px;
    display: flex; align-items: center; gap: 14px;
    color: var(--navy);
    font-weight: 600;
  }
  .brand-dot {
    width: 54px; height: 54px; border-radius: 50%;
    background: var(--navy);
    flex: none;
  }
  .brand-name { font-size: 24px; line-height: 1.15; }
  .brand-name span { display: block; font-size: 15px; letter-spacing: 2px; }
  .person {
    position: absolute;
    right: 40px; top: 150px;
    text-align: right;
  }
  .person .name { color: var(--royal); font-weight: 700; font-size: 19px; }
  .person .role { color: var(--muted); font-size: 14px; }
  .contact {
    position: absolute;
    left: 44px; top: 232px;
    list-style: none;
    color: var(--ink);
    font-size: 12px;
    line-height: 20px;
  }
  .contact li { display: flex; align-items: center; gap: 8px; white-space: nowrap; }
  .contact svg { width: 11px; height: 11px; fill: var(--royal); flex: none; }
  .card-front .web {
    position: absolute;
    right: 40px; bottom: 22px;
    color: var(--paper);
    font-size: 14px;
    letter-spacing: 1.5px;
    white-space: nowrap;
  }
</style>
</head>
<body>
  <section class="card card-back" aria-label="Card back">
    <p class="web">www.<strong>kvrdpinecrestrehab</strong>.example</p>
  </section>

  <section class="card card-front" aria-label="Card front">
    <svg class="band" viewBox="0 0 620 120" preserveAspectRatio="none" aria-hidden="true">
      <defs>
        <linearGradient id="bandFill" x1="0" y1="0" x2="1" y2="0">
          <stop offset="0" stop-color="#4a72d6"/>
          <stop offset="1" stop-color="#23409c"/>
        </linearGradient>
      </defs>
      <path d="M0 112 C200 105 380 80 620 40 L620 120 L0 120 Z" fill="url(#bandFill)" opacity="0.35"/>
      <path d="M0 116 C220 110 400 90 620 58 L620 120 L0 120 Z" fill="url(#bandFill)"/>
    </svg>

    <div class="brand">
      <span class="brand-dot"></span>
      <p class="brand-name">KVRD Pinecrest<span>REHABILITATION</span></p>
    </div>

    <div class="person">
      <p class="name">Dorian K. Lumbard, Ph. D.</p>
      <p class="role">Owner</p>
    </div>

    <ul class="contact">
      <li><svg viewBox="0 0 12 12"><path d="M3 1l2 2.5-1.2 1.2a7 7 0 0 0 3.5 3.5L8.5 7 11 9l-1.5 2C5 11 1 7 1 2.5z"/></svg>770.555.0182</li>
      <li><svg viewBox="0 0 12 12"><path d="M1 3h10v6H1z"/></svg>Dorian.Lumbard@kvrdpinecrestrehab.example</li>
      <li><svg viewBox="0 0 12 12"><path d="M6 0a4 4 0 0 0-4 4c0 3 4 8 4 8s4-5 4-8a4 4 0 0 0-4-4z"/></svg>4173b GA Hwy 508 STE 612 Conyers, GA 30081</li>
    </ul>

    <p class="web">www.<strong>kvrdpinecrestrehab</strong>.example</p>
  </section>
</body>
</html>
```